TELURIN WEB DESIGN (please use the uploaded photos)

We are looking for a web design that captures the essence of Telurin: authenticity, connection with nature, and simplicity. We want the page to convey the story of our brand, from its cultural significance to its commitment to quality and authenticity. Additionally, we need to integrate Telurin's sub-brands, such as BOSRE, our line of healthy pecan nut snacks.

Design Objective:
We want our website to be more than just a product showcase: it should be a reflection of our brand identity and a platform that inspires our customers to connect with us on a deeper level.

Company Background:
Telurin is a company specializing in walnut production, hunting ranch management, and livestock. The name "Telurin" means "FOUR" in the PIMA dialect, in honor of the Pima communities that once inhabited the ranch. This historical and cultural connection is at the heart of our brand.

Audience Needs and Aspirations:
All our customers share deep emotional needs. They seek authenticity, honesty, and a happy, simple life. They want to reconnect with their natural state, dream, return to simplicity, and renew their hopes.

Brand Archetype:
Inspired by the archetypes of Greta, Tobias Wrenfield, and Innocent, we aim to reflect the need to be oneself, honesty, and authenticity in all aspects.

Brand Objective:
Our mission is to reconnect our customers with their natural state, offering high-quality products that simplify their lives and inspire them to dream and renew their hopes.

Key Design Elements:

Natural and earthy color palette reflecting our connection to nature.
Images and graphics depicting ranch life, walnut production, and the quality of our products.
Clean and easy-to-navigate design to reflect our philosophy of simplicity and honesty.
Seamless and clear integration of sub-brands, such as BOSRE.

Target Market(s)

Organic Women (30-50 years) committed to exercise and healthy diets. Hunters (40-60 years) with a deeply rooted conservative mindset. Prime Men (40-60 years) with high income, power, and status.

Coding

Coded - Design and coding required

Number of Pages Required

4 page

Other font styles liked:
• Brother 1816 Printed

Requirements
Must have
• Authenticity and Nature Connection: Reflect the brand's authenticity and connection to nature through design elements. Simplicity and Navigation: Keep the design clean and easy to navigate. Integration of Sub-brands: Seamlessly incorporate sub-brands like BOSRE into the design. Quality Imagery: Use high-quality visuals to showcase products and brand essence. Responsive Design: Ensure the website looks and functions well across different devices. Storytelling: Incorporate storytelling to convey the brand's history, values, and culture. Clear CTAs: Include clear calls-to-action to guide visitors towards desired actions.
Nice to have
• I have the telurinhq.com Domain, also I'm working on WIX

```html
<!DOCTYPE html>
<html lang="en">
<head>
<meta charset="utf-8">
<title>Telurin</title>
<link href="https://fonts.googleapis.com/css2?family=Outfit:wght@300;400;500;600;700&display=swap" rel="stylesheet">
<style>
:root{
  --orange:#d8431c;
  --ink:#2e2e2e;
  --text:#4a4a4a;
  --dark:#3d3d3d;
  --footer:#262626;
  --topbar:#2b2b2b;
  --white:#ffffff;
  --muted:#8a8a8a;
  --star:#f2b01e;
}
*{box-sizing:border-box;margin:0;padding:0}
html,body{width:1200px;height:4367px;overflow:hidden}
body{font-family:"Outfit",sans-serif;color:var(--text);background:var(--white);position:relative}
.abs{position:absolute}
.section{position:absolute;left:0;width:1200px}
.btn{position:absolute;background:var(--orange);color:var(--white);font-size:16px;font-weight:500;display:flex;align-items:center;justify-content:center}
.photo{position:absolute}

/* top bar */
.topbar{top:0;height:42px;background:var(--topbar);color:#bdbdbd;font-size:15px}
.topbar .social{left:86px;top:12px;display:flex;gap:12px;font-size:12px;color:#d0d0d0}
.topbar .contact{top:11px;display:flex;align-items:center;gap:7px}
.topbar svg{stroke:var(--orange);fill:none;stroke-width:2}

/* nav */
.nav{top:42px;height:90px;background:var(--white)}
.logo{display:flex;align-items:center;gap:10px;font-weight:500;letter-spacing:1px}
.logo .mark{width:14px;height:14px;background:var(--orange)}
.nav .logo{left:88px;top:28px;font-size:31px;color:var(--ink)}
.nav .links{right:0;top:0;height:90px}
.nav .link{position:absolute;top:36px;font-size:16px;color:var(--ink);font-weight:500}

/* hero */
.hero{top:132px;height:526px;background:radial-gradient(ellipse at 55% 55%,#6f7a3c 0%,#4a4a2a 30%,#2d2a1f 65%,#1c1b17 100%)}
.hero h1{position:absolute;top:160px;width:100%;text-align:center;color:var(--white);font-weight:300;font-size:53px;line-height:70px}

/* split sections */
.eyebrow{color:var(--orange);font-weight:600;font-size:18px}
.h2{font-weight:300;font-size:42px;color:var(--ink)}
.para{font-size:16px;line-height:26.6px;color:var(--text)}
.notched{clip-path:polygon(0 0,100% 0,100% 100%,215px 100%,173px calc(100% - 52px),0 calc(100% - 52px));border-radius:14px}
.band{position:absolute;background:var(--orange);height:48px;width:168px}

.about{top:658px;height:659px}
.values{top:1317px;height:658px;background:var(--dark)}
.values .h2,.values .para{color:var(--white)}
.culture{top:1975px;height:657px}
.culture .item{position:absolute;left:85px;width:490px;display:flex;gap:20px}
.culture .icon{width:82px;height:82px;border-radius:12px;background:var(--orange);flex:none}
.culture .item p{font-size:15.5px;line-height:24px;color:var(--text);margin-top:-2px}

/* products */
.products{top:2632px;height:660px;background:var(--dark)}
.products .h2{position:absolute;top:74px;width:100%;text-align:center;color:var(--white)}
.card{position:absolute;top:168px;width:322px}
.card .frame{height:254px;border:1.5px solid var(--orange);border-radius:12px;position:relative}
.card .pic{position:absolute;left:0;top:10px;right:10px;bottom:2px;border-radius:10px}
.card h3{font-weight:400;font-size:22px;color:var(--white);margin-top:16px}
.card p{font-size:15px;line-height:24px;color:#e4e4e4;margin-top:6px;height:72px}
.more{display:inline-flex;align-items:center;gap:6px;color:var(--orange);font-size:16px;font-weight:500;border-bottom:1px solid var(--orange);padding-bottom:3px;margin-top:10px}

/* reviews */
.reviews{top:3292px;height:662px;text-align:center}
.reviews .eyebrow{position:absolute;top:62px;width:100%}
.reviews .h2{position:absolute;top:88px;width:100%;font-size:46px;line-height:50px}
.review{position:absolute;top:220px;width:310px}
.avatar{width:98px;height:98px;border-radius:50%;margin:0 auto;position:relative;background:radial-gradient(circle at 50% 40%,#c9a489 0%,#7a5b48 55%,#3b3532 100%)}
.avatar .q{position:absolute;right:-26px;bottom:-18px;color:var(--orange);font-size:62px;font-weight:700;line-height:1}
.review blockquote{font-style:italic;font-size:16.5px;line-height:26.5px;color:var(--text);margin-top:30px}
.stars{display:flex;justify-content:center;gap:3px;margin-top:14px}
.review .name{font-weight:600;font-size:17px;color:var(--ink);margin-top:14px}
.review .role{font-style:italic;font-size:14px;color:var(--muted);margin-top:4px}
.dots{position:absolute;top:605px;left:570px;display:flex;gap:9px;align-items:center}
.dots span{width:5px;height:5px;border-radius:50%;background:#b0b0b0}
.dots .on{width:28px;height:5px;border-radius:3px;background:var(--orange)}

/* footer */
.footer{top:3954px;height:413px;background:var(--footer);color:#b8b8b8}
.footer .logo{left:85px;top:95px;font-size:44px;color:var(--white)}
.footer .logo .mark{width:18px;height:18px}
.footer .about-text{left:85px;top:172px;width:290px;font-size:15.5px;line-height:26px}
.vline{position:absolute;top:85px;height:245px;width:1px;background:#555}
.vline::after{content:"";position:absolute;left:-1px;top:68px;width:3px;height:26px;background:var(--orange)}
.ftitle{position:absolute;top:107px;color:var(--orange);font-weight:600;font-size:17px;letter-spacing:.5px}
.finfo{position:absolute;left:486px;display:flex;gap:14px;font-size:15px;line-height:24px}
.finfo svg{flex:none;margin-top:4px;stroke:#ddd;fill:none;stroke-width:1.8}
.flinks{position:absolute;left:815px;top:150px;font-size:15.5px;line-height:38px}
.fsocial{position:absolute;left:1013px;top:156px;display:flex;gap:14px;font-size:13px;color:#ddd}
.copyright{position:absolute;bottom:36px;left:85px;font-size:14px;color:#8a8a8a}
.copyright b{color:var(--orange);font-weight:400}
.date{position:absolute;bottom:36px;right:86px;font-size:14px;color:#8a8a8a}
</style>
</head>
<body>

<header class="section topbar">
  <div class="abs social"><span>Nookly</span><span>Quillo</span><span>Snapwell</span></div>
  <div class="abs contact" style="left:803px">
    <svg width="16" height="13" viewBox="0 0 16 13"><rect x="1" y="1" width="14" height="11" rx="1"/><path d="M1 2l7 5 7-5"/></svg>
    <span>info@telurinhq.com</span>
  </div>
  <div class="abs contact" style="left:990px">
    <svg width="15" height="15" viewBox="0 0 24 24"><path d="M5 3h4l2 5-3 2a12 12 0 0 0 6 6l2-3 5 2v4a2 2 0 0 1-2 2A18 18 0 0 1 3 5a2 2 0 0 1 2-2z"/></svg>
    <span>1800-555-210</span>
  </div>
</header>

<nav class="section nav">
  <div class="abs logo"><span class="mark"></span><span>TELURIN</span></div>
  <a class="link" style="left:675px">Home</a>
  <a class="link" style="left:773px">About</a>
  <a class="link" style="left:871px">Bosre</a>
  <a class="btn" style="left:946px;top:27px;width:132px;height:38px">Contact</a>
</nav>

<section class="section hero" role="img" aria-label="Weathered hands holding freshly harvested green pecan husks">
  <h1>Offering high-quality products<br>that simplify their lives and inspire</h1>
  <a class="btn" style="left:508px;top:319px;width:148px;height:36px;font-size:15px">Discover More</a>
</section>

<section class="section about">
  <div class="abs eyebrow" style="left:83px;top:126px">Brand's History</div>
  <h2 class="abs h2" style="left:83px;top:150px">About Telurin</h2>
  <p class="abs para" style="left:85px;top:218px;width:500px">Lorem ipsum dolor sit amet, consectetur adipiscing elit. Aliquam eget feugiat velit. Curabitur tincidunt maximus lorem sit amet venenatis. Sed cursus tortor sed porttitor tempus. Sed sit amet dapibus enim, eu facilisis sapien. Nunc mi nisl, porta eu turpis id, suscipit mattis turpis. Nullam at augue a meliquet pellentesque. Phasellus a finibus neque, vel facilisis mi. Aliquam molestie massa nec lectus ullamcorper ullamcorper.</p>
  <a class="btn" style="left:85px;top:435px;width:147px;height:38px">Read More</a>
  <div class="photo notched" style="left:649px;top:106px;width:463px;height:419px;background:linear-gradient(180deg,#1c2b3d 0%,#2a3a4a 45%,#6b6a55 75%,#3a3a2e 100%)" role="img" aria-label="Small white ranch cabin among tall cacti under a night sky"></div>
  <div class="band" style="left:652px;top:478px"></div>
</section>

<section class="section values">
  <div class="photo" style="left:85px;top:144px;width:480px;height:368px;border-radius:14px;background:linear-gradient(180deg,#c9cdd0 0%,#5d7040 35%,#44552e 60%,#8a7a60 100%)" role="img" aria-label="Group of orchard workers standing with buckets and poles between rows of pecan trees"></div>
  <h2 class="abs h2" style="left:619px;top:185px;font-size:37px">Our Values</h2>
  <p class="abs para" style="left:620px;top:248px;width:490px;font-size:19px;line-height:31px">Lorem ipsum dolor sit amet, consectetur adipiscing elit. Aliquam eget feugiat velit. Curabitur tincidunt maximus lorem sit amet venenatis. Sed cursus tortor sed porttitor tempus. Sed sit amet dapibus enim,</p>
  <a class="btn" style="left:620px;top:407px;width:146px;height:39px">Read More</a>
</section>

<section class="section culture">
  <h2 class="abs h2" style="left:84px;top:108px;font-size:38px">Our Culture</h2>
  <p class="abs" style="left:85px;top:158px;width:495px;font-size:15.5px;line-height:27px;font-weight:600;color:var(--ink)">Curabitur tincidunt maximus lorem sit amet venenatis. Sed cursus tortor sed porttitor tempus. Sed sit ibus enim, eu facilisis sapien.</p>
  <div class="item" style="top:254px"><div class="icon" role="img" aria-label="Pecan nut icon"></div><p>Nullam at augue a melit pellentesque. Phasellus a finibus neque, vel facilisis mi. Aliquam molestie massa nec lectus ullamcorper ullamcorper.</p></div>
  <div class="item" style="top:352px"><div class="icon" role="img" aria-label="Hunting target with deer icon"></div><p>Nullam at augue a melit pellentesque. Phasellus a finibus neque, vel facilisis mi. Aliquam molestie massa nec lectus ullamcorper ullamcorper.</p></div>
  <div class="item" style="top:451px"><div class="icon" role="img" aria-label="Livestock and fence icon"></div><p>Nullam at augue a melit pellentesque. Phasellus a finibus neque, vel facilisis mi. Aliquam molestie massa nec lectus ullamcorper ullamcorper.</p></div>
  <div class="photo notched" style="left:649px;top:113px;width:463px;height:421px;background:linear-gradient(180deg,#d9a068 0%,#8a6a50 28%,#4e4530 55%,#3a3526 100%)" role="img" aria-label="Aerial view of pecan orchard rows and a dirt road at sunset"></div>
  <div class="band" style="left:652px;top:487px"></div>
</section>

<section class="section products">
  <h2 class="h2">Our Product</h2>
  <div class="card" style="left:85px">
    <div class="frame"><div class="pic" style="background:linear-gradient(160deg,#4e6a38,#2e4224)" role="img" aria-label="Green pecan husks on a tree branch"></div></div>
    <h3>Duis scelerisque rius nulla</h3>
    <p>Premium pecan oil, carefully extracted to retain its natural flavor and hl properties, making it an ideal op culinary</p>
    <a class="more">Read More <span>→</span></a>
  </div>
  <div class="card" style="left:437px">
    <div class="frame"><div class="pic" style="background:linear-gradient(180deg,#9fb2a8 0%,#5f6b42 45%,#6e5f48 100%)" role="img" aria-label="Two workers filling a sack with harvested pecans"></div></div>
    <h3>Sed eget nulla non ante mollis</h3>
    <p>Unique beauty product line based on the benefits of pecan. Our products harness pecan oil's nourishing and reparative</p>
    <a class="more">Read More <span>→</span></a>
  </div>
  <div class="card" style="left:792px">
    <div class="frame"><div class="pic" style="background:linear-gradient(135deg,#4a5040,#6a6a5a 50%,#3e4436)" role="img" aria-label="Aerial view of crossing orchard lanes"></div></div>
    <h3>Nulla non faucibus nunc</h3>
    <p>A versatile and nutritious option for all your baking needs.</p>
    <a class="more">Read More <span>→</span></a>
  </div>
</section>

<section class="section reviews">
  <div class="eyebrow">Client Review</div>
  <h2 class="h2">What Our Customers<br>Are Saying</h2>
  <div class="review" style="left:86px">
    <div class="avatar" role="img" aria-label="Customer portrait"><span class="q">”</span></div>
    <blockquote>Duis consequat tor et nunc tristique, id aliquet ligula efficitur. Cras at laoreet metus, non molestie lacus. Pellentesque metus mauris, ultrices vitae nunc eu, inteauctor leo.</blockquote>
    <div class="stars"><svg width="92" height="16" viewBox="0 0 92 16" fill="var(--star)"><g id="st"><path d="M8 0l2.4 5 5.4.6-4 3.7 1.1 5.4L8 12 3.1 14.7l1.1-5.4-4-3.7 5.4-.6z"/></g><use href="#st" x="19"/><use href="#st" x="38"/><use href="#st" x="57"/><use href="#st" x="76"/></svg></div>
    <div class="name">Aldo Vance</div>
    <div class="role">Customer</div>
  </div>
  <div class="review" style="left:443px">
    <div class="avatar" role="img" aria-label="Customer portrait"><span class="q">”</span></div>
    <blockquote>Duis consequat tor et nunc tristique, id aliquet ligula efficitur. Cras at laoreet metus, non molestie lacus. Pellentesque metus mauris, ultrices vitae nunc eu, inteauctor leo.</blockquote>
    <div class="stars"><svg width="92" height="16" viewBox="0 0 92 16" fill="var(--star)"><use href="#st"/><use href="#st" x="19"/><use href="#st" x="38"/><use href="#st" x="57"/><use href="#st" x="76"/></svg></div>
    <div class="name">Nessa Orrin</div>
    <div class="role">Customer</div>
  </div>
  <div class="review" style="left:801px">
    <div class="avatar" role="img" aria-label="Customer portrait"><span class="q">”</span></div>
    <blockquote>Duis consequat tor et nunc tristique, id aliquet ligula efficitur. Cras at laoreet metus, non molestie lacus. Pellentesque metus mauris, ultrices vitae nunc eu, inteauctor leo.</blockquote>
    <div class="stars"><svg width="92" height="16" viewBox="0 0 92 16" fill="var(--star)"><use href="#st"/><use href="#st" x="19"/><use href="#st" x="38"/><use href="#st" x="57"/><use href="#st" x="76"/></svg></div>
    <div class="name">Pell Dunmore</div>
    <div class="role">Customer</div>
  </div>
  <div class="dots"><span class="on"></span><span></span><span></span></div>
</section>

<footer class="section footer">
  <div class="abs logo"><span class="mark"></span><span>TELURIN</span></div>
  <p class="abs about-text">Lorem ipsum dolor sit , consectetur adipiscing elit. Aliquam eget feugiat velit. Curabitur tincidunt maximus lorem sit amet venenatis.</p>
  <span class="vline" style="left:424px"></span>
  <span class="vline" style="left:756px"></span>
  <span class="vline" style="left:970px"></span>
  <div class="ftitle" style="left:486px">CONTACT INFO</div>
  <div class="finfo" style="top:150px">
    <svg width="16" height="16" viewBox="0 0 24 24"><path d="M12 2l9 10-9 10-9-10z"/><circle cx="12" cy="12" r="3"/></svg>
    <span>45 BC, making it over<br>Larkmoor, Valdena</span>
  </div>
  <div class="finfo" style="top:210px">
    <svg width="16" height="13" viewBox="0 0 16 13"><rect x="1" y="1" width="14" height="11" rx="1"/><path d="M1 2l7 5 7-5"/></svg>
    <span>info@telurinhq.com</span>
  </div>
  <div class="finfo" style="top:244px">
    <svg width="16" height="16" viewBox="0 0 24 24"><path d="M5 3h4l2 5-3 2a12 12 0 0 0 6 6l2-3 5 2v4a2 2 0 0 1-2 2A18 18 0 0 1 3 5a2 2 0 0 1 2-2z"/></svg>
    <span>1800-555-210</span>
  </div>
  <div class="ftitle" style="left:815px">QUICK LINKS</div>
  <div class="flinks">Home<br>About<br>Bosre<br>Contact</div>
  <div class="ftitle" style="left:1013px">FOLLOW US</div>
  <div class="fsocial"><span>Nookly</span><span>Quillo</span></div>
  <div class="fsocial" style="top:180px"><span>Snapwell</span></div>
  <div class="copyright">© 2024 <b>TELURIN</b>. All right reserved</div>
  <div class="date">March 14, 2024. Layout_4</div>
</footer>

</body>
</html>
```